Valentine's Day Flyer

We require an A5 size flyer to promote our February parking offer & Giveaway.

Offer:
Book your parking online & Save!
$5 Night/Weekend Parking
$10 Early Bird Parking

Giveaway: Win a $5,000 Diamond Ring!
Every time you book your parking online using Park-n-Hold you get a chance to win!

The final design should contain:
- Valentine's Theme
- Emphasise 'Book your parking online & Save!'

Designers: please visit www.bayvaultlots.com.au for more info on Bayvault Parking & Park-n-Hold

Target Market(s)

18-50 year old drivers

Industry/Entity Type

Parking

```html
<!DOCTYPE html>
<html lang="en">
<head>
<meta charset="utf-8">
<title>Park-n-Hold Valentine's Parking Flyer</title>
<link rel="stylesheet" href="https://fonts.googleapis.com/css2?family=Dosis:wght@300;400;600&family=Bitter:wght@400;500&family=Open+Sans:wght@400&display=swap">
<style>
  :root {
    --page-bg: #e8e3dc;
    --flyer-bg: #231f20;
    --yellow: #f9c82b;
    --white: #ffffff;
    --ink: #231f20;
    --soft-white: #f1f1f1;
  }
  * { box-sizing: border-box; margin: 0; padding: 0; }
  html, body {
    width: 892px;
    height: 1200px;
    overflow: hidden;
    background: var(--page-bg);
  }
  .flyer {
    position: absolute;
    left: 56px;
    top: 40px;
    width: 780px;
    height: 1120px;
    background: var(--flyer-bg);
    box-shadow: 0 4px 14px rgba(0,0,0,0.25);
    font-family: "Dosis", sans-serif;
    color: var(--soft-white);
  }
  .kicker {
    position: absolute;
    left: 39px;
    top: 50px;
    font-weight: 300;
    font-size: 36px;
    letter-spacing: 0.5px;
    color: var(--white);
  }
  .headline {
    position: absolute;
    left: 36px;
    top: 104px;
    font-weight: 300;
    font-size: 82px;
    line-height: 1;
    letter-spacing: 1px;
    color: var(--yellow);
  }
  .hero-art {
    position: absolute;
    left: 0;
    top: 238px;
    width: 780px;
    height: 270px;
    background:
      radial-gradient(ellipse 110px 95px at 505px 95px, rgba(249,200,43,0.9) 0%, rgba(249,200,43,0.6) 55%, rgba(249,200,43,0) 100%),
      linear-gradient(90deg, #2a2627 0%, #343031 50%, #2a2627 100%);
    border-bottom: 2px solid var(--white);
  }
  .intro {
    position: absolute;
    left: 62px;
    top: 537px;
    width: 600px;
    font-weight: 300;
    font-size: 36px;
    line-height: 48px;
    color: var(--white);
  }
  .intro .product { color: var(--yellow); }
  .rates {
    position: absolute;
    left: 60px;
    top: 692px;
    list-style: none;
    font-family: "Bitter", serif;
    color: var(--white);
  }
  .rates li { font-size: 30px; line-height: 56px; }
  .rates .price { font-size: 36px; font-weight: 500; margin-right: 6px; }
  .prize {
    position: absolute;
    left: 38px;
    top: 828px;
    width: 702px;
    height: 86px;
    background: var(--white);
    border-radius: 10px;
    display: flex;
    align-items: center;
    justify-content: center;
    font-family: "Bitter", serif;
    font-size: 43px;
    font-weight: 500;
    color: var(--ink);
  }
  .prize .amount { font-size: 58px; margin: 0 10px; }
  .brand {
    position: absolute;
    left: 38px;
    top: 946px;
    height: 72px;
    display: flex;
    align-items: center;
    gap: 14px;
  }
  .brand-mark {
    width: 22px;
    height: 22px;
    background: var(--yellow);
  }
  .brand-name {
    font-family: "Dosis", sans-serif;
    font-weight: 600;
    font-size: 44px;
    color: var(--white);
  }
  .contact {
    position: absolute;
    display: flex;
    align-items: center;
    gap: 7px;
    font-family: "Open Sans", sans-serif;
    font-size: 21px;
    color: var(--yellow);
    white-space: nowrap;
  }
  .contact svg { flex: none; }
  .contact-web { left: 424px; top: 968px; }
  .contact-address { left: 48px; top: 1045px; }
  .contact-phone { left: 558px; top: 1045px; }
</style>
</head>
<body>
  <main class="flyer">
    <p class="kicker">BOOK YOUR PARKING</p>
    <h1 class="headline">ONLINE &amp; SAVE!</h1>

    <div class="hero-art" role="img" aria-label="Valentine's illustration: a row of white outlined hearts whose tails curve into a road, ending in a solid yellow heart, with a white car parked beside a parking sign"></div>

    <p class="intro">Every time you book your parking online using <span class="product">Park-n-Hold</span> you get a chance to WIN</p>

    <ul class="rates">
      <li><span class="price">$5</span>Night/Weekend Parking</li>
      <li><span class="price">$10</span>Early Bird Parking</li>
    </ul>

    <p class="prize">Win a <span class="amount">$5000</span> Diamond Ring</p>

    <div class="brand">
      <span class="brand-mark"></span>
      <span class="brand-name">Bayvault Parking</span>
    </div>

    <p class="contact contact-web">
      <svg width="20" height="20" viewBox="0 0 20 20" fill="none" stroke="#f9c82b" stroke-width="1.4">
        <circle cx="10" cy="10" r="8.5"/>
        <ellipse cx="10" cy="10" rx="3.8" ry="8.5"/>
        <line x1="1.5" y1="10" x2="18.5" y2="10"/>
        <path d="M3 5.5h14M3 14.5h14"/>
      </svg>
      www.bayvaultlots.com.au
    </p>

    <p class="contact contact-address">
      <svg width="16" height="22" viewBox="0 0 16 22">
        <path d="M8 0C3.6 0 0 3.5 0 7.9 0 13.6 8 22 8 22s8-8.4 8-14.1C16 3.5 12.4 0 8 0zm0 11a3 3 0 1 1 0-6 3 3 0 0 1 0 6z" fill="#f9c82b"/>
      </svg>
      48 Carrow Street Eastlake, NSW 2061
    </p>

    <p class="contact contact-phone">
      <svg width="22" height="22" viewBox="0 0 22 22" fill="none" stroke="#f9c82b" stroke-width="1.4">
        <circle cx="11" cy="11" r="10"/>
        <path d="M7.5 5.5l2 2.3-1.2 1.6c.8 1.8 2.1 3.1 3.8 3.9l1.6-1.2 2.3 2-1.3 1.9c-4-.6-7.3-3.9-8-8z" fill="#f9c82b" stroke="none"/>
      </svg>
      1300 555 019
    </p>
  </main>
</body>
</html>
```